BrivoMatex. Lantern for the Steady Growth. Business card

Professional business card for BrivoMatex (Lantern for the Steady Growth)
My rationale: Strategy-> Execution-> Results-> Value that lead to the BrivoMatex name: We put the Lantern for the Steady Growth.
We deliver value to our customers helping them at defining a good strategy (cyan arrow). 90% of well formulated strategies fail due to poor execution so we also consider strategical execution very important (green arrow). Due to the execution we obtain the results (blue arrow). Finally, the results provide feedback to redefine strategy, and the new strategy has to be executed and new results obtained providing new feedback and on and on. It's like a wheel that finally, must create corporate value: value for shareholders, staholders, employees, providers...-

Target Market(s)

CEOs and steering comitees , invewrnent funds

Industry/Entity Type

Business Consultant

Contact Information for Business Card

Tommaso Ferlini
CEO & Founder
tommaso.ferlini@brivomatex.example
Mobile: +34 611.205.938
www.brivomatex.example

Colors

Designer to choose colors to be used in the design.

Requirements
Nice to have
• Nice to hace the words: Strategy, execution, results
• Nice to vave the claim: Lantern for the Steady Growth
• The three colors should be shown:
• cyan for STRATEGY
• green for EXECUTION
• blue for RESULTS
Should not have
• Complete black background

```html
<!DOCTYPE html>
<html lang="en">
<head>
<meta charset="utf-8">
<title>BrivoMatex — Business Card</title>
<link href="https://fonts.googleapis.com/css2?family=PT+Sans+Narrow:wght@700&family=Arimo:wght@400&display=swap" rel="stylesheet">
<style>
  :root {
    --stage: #252525;
    --card-white: #ffffff;
    --brand-blue: #0a3a9e;
    --text-grey: #444444;
    --text-dark: #1e1e1e;
    --lime: #9bc92d;
    --cyan: #1aa6e6;
    --deep-blue: #0b3fa3;
    --tagline: #ffffff;
  }
  * { margin: 0; padding: 0; box-sizing: border-box; }
  html, body {
    width: 1200px; height: 900px; overflow: hidden;
    background: var(--stage);
  }
  .stage { position: relative; width: 1200px; height: 900px; }

  .card {
    position: absolute; top: 200px; width: 310px; height: 502px;
    box-shadow: 3px 4px 6px rgba(0,0,0,0.45);
  }

  /* Front */
  .card-front {
    left: 253px;
    background: var(--card-white);
    border-radius: 52px 0 52px 0;
  }
  .front-brand {
    position: absolute; left: 0; right: 0; top: 368px;
    top: 368px;
    text-align: center;
    font-family: "PT Sans Narrow", "Arial Narrow", sans-serif;
    font-weight: 700; font-size: 46px; line-height: 1;
    color: var(--brand-blue);
  }
  .front-brand { top: 166px; }
  .person { position: absolute; left: 24px; top: 329px; }
  .person-name {
    font-family: "Arimo", Arial, sans-serif;
    font-size: 19px; color: var(--brand-blue); line-height: 1.1;
  }
  .person-role {
    font-family: "Arimo", Arial, sans-serif;
    font-size: 14px; color: var(--text-grey); margin-top: 3px;
  }
  .contact-list {
    position: absolute; left: 24px; top: 403px;
    list-style: none;
    font-family: "Arimo", Arial, sans-serif;
    font-size: 14px; color: var(--text-dark); line-height: 18.5px;
  }
  .contact-list li { display: flex; align-items: center; gap: 4px; }
  .contact-icon { width: 14px; height: 12px; flex: none; }
  .web-prefix { color: var(--brand-blue); }
  .web-name { color: var(--lime); }
  .web-suffix { color: var(--cyan); }

  /* Back */
  .card-back {
    left: 627px;
    border-radius: 0 52px 0 52px;
    overflow: hidden;
    background:
      radial-gradient(ellipse 260px 220px at 0% 100%, rgba(11,63,163,0.95), rgba(11,63,163,0) 100%),
      radial-gradient(ellipse 300px 260px at 100% 0%, rgba(10,168,240,1), rgba(10,168,240,0) 100%),
      linear-gradient(160deg, #5fcc7a 0%, #9bc92d 45%, #92c731 70%, #3a8fb0 100%);
  }
  .back-decoration { position: absolute; inset: 0; }
  .back-brand {
    position: absolute; left: 0; right: 0; top: 226px;
    text-align: center;
    font-family: "PT Sans Narrow", "Arial Narrow", sans-serif;
    font-weight: 700; font-size: 52px; line-height: 1;
    color: var(--brand-blue);
  }
  .back-tagline {
    position: absolute; left: 0; right: 0; top: 289px;
    text-align: center;
    font-family: "Arimo", Arial, sans-serif;
    font-size: 12.5px; letter-spacing: 0.2px;
    color: var(--tagline); text-transform: uppercase;
  }
</style>
</head>
<body>
<main class="stage">

  <section class="card card-front">
    <div class="front-brand">BrivoMatex</div>

    <div class="person">
      <p class="person-name">Tommaso Ferlini</p>
      <p class="person-role">CEO &amp; Founder</p>
    </div>

    <ul class="contact-list">
      <li>
        <svg class="contact-icon" viewBox="0 0 14 12" aria-hidden="true">
          <path d="M1 4.5C1 2 4 1 7 1s6 1 6 3.5h-3V3.5H4v1z" fill="#0a3a9e"/>
          <rect x="2.5" y="5.5" width="9" height="5.5" rx="1" fill="#0a3a9e"/>
          <circle cx="7" cy="8.2" r="1.4" fill="#fff"/>
        </svg>
        <span>+34 611.205.938</span>
      </li>
      <li>
        <svg class="contact-icon" viewBox="0 0 14 12" aria-hidden="true">
          <rect x="0.5" y="1.5" width="13" height="9" fill="#0a3a9e"/>
          <path d="M1 2l6 5 6-5" fill="none" stroke="#fff" stroke-width="1.2"/>
        </svg>
        <span>tommaso.ferlini@brivomatex.example</span>
      </li>
      <li>
        <svg class="contact-icon" viewBox="0 0 14 12" aria-hidden="true">
          <circle cx="7" cy="6" r="5.5" fill="#0a3a9e"/>
          <path d="M4 4c1 0 2 1 1.5 2S4 7 5 8.5M9 2.5c0 1.5 1.5 1.5 2 3-1 1-2 0-2.5 1.5" fill="none" stroke="#fff" stroke-width="1"/>
        </svg>
        <span><span class="web-prefix">www.</span><span class="web-name">brivomatex</span><span class="web-suffix">.example</span></span>
      </li>
    </ul>
  </section>

  <section class="card card-back">
    <div class="back-decoration" role="img" aria-label="Soft gradient field of cyan, green and blue behind the brand name"></div>
    <div class="back-brand">BrivoMatex</div>
    <p class="back-tagline">Lantern for the Steady Growth</p>
  </section>

</main>
</body>
</html>
```